Simplified minimalist but bold website

Design a website for a brand 'Gather Every Moment' that shares ideas to make managing home and health easier through email swap series, webinars and eventually courses.

Simple landing page to attract users to sign up for a freebie.

Target Market(s)

women with families & homes to run

Number of Pages Required

1 page

Font styles to use
Sans Serif

Colors
e667a6
b768aa
acd136
ffffff
959595

Requirements
Must have
• Simplified look, line icons, opt-in template, contact us form

```html
<!DOCTYPE html>
<html lang="en">
<head>
<meta charset="utf-8">
<title>Gather Every Moment</title>
<link href="https://fonts.googleapis.com/css2?family=Abel&family=Fjalla+One&family=Open+Sans:wght@400;700&display=swap" rel="stylesheet">
<style>
:root{
  --bg:#f8ee9c;
  --pink:#e667a6;
  --purple:#b768aa;
  --purple-deep:#8e4f9a;
  --green:#acd136;
  --white:#ffffff;
  --grey:#959595;
  --ink:#3a3a3a;
  --blue:#3b8fd0;
  --blue-deep:#1f5f8e;
  --footer:#1fb3e3;
}
*{box-sizing:border-box;margin:0;padding:0}
html,body{width:1200px;height:3724px;overflow:hidden}
body{background:var(--bg);font-family:'Abel',sans-serif;color:var(--ink);position:relative}
.abs{position:absolute}
.photo{position:absolute}

/* hero */
.hero{left:0;top:0;width:1200px;height:330px;background:linear-gradient(135deg,#f3d9e3 0%,#fbf1f4 45%,#e9cbd8 100%)}
.nav{left:0;top:0;width:1200px;height:40px;display:flex;justify-content:center;gap:64px;padding-top:4px}
.nav a{color:var(--white);font-family:'Fjalla One',sans-serif;font-size:30px;text-decoration:none;letter-spacing:.5px}
.hero-title{left:0;top:150px;width:1200px;text-align:center;font-family:'Abel',sans-serif;font-size:58px;color:var(--white);font-weight:400}
.hero-sub{left:0;top:230px;width:1200px;text-align:center;color:var(--pink);font-size:22px}
.btn{display:inline-block;border:none;color:var(--white);font-family:'Abel',sans-serif;text-align:center;border-radius:6px}
.btn-green{background:var(--green)}
.btn-purple{background:var(--purple)}
.hero-btn{left:545px;top:280px;width:110px;height:28px;line-height:28px;font-size:18px}

/* intro */
.intro-photo{left:50px;top:338px;width:430px;height:200px;background:linear-gradient(120deg,#9a8f86,#d7cbbf 50%,#6d6a6e)}
.intro-text{left:520px;top:345px;width:500px;text-align:center;font-size:28px;line-height:44px;color:var(--ink)}
.intro-btn{left:640px;top:536px;width:270px;height:42px;line-height:42px;font-size:28px;font-family:'Fjalla One',sans-serif}

/* rose signup */
.rose-photo{left:270px;top:595px;width:330px;height:405px;background:radial-gradient(circle at 45% 45%,#e98fb4,#c75a8a 45%,#e6dfe6 75%)}
.rose-text{left:620px;top:660px;width:420px;font-size:13px;line-height:18px;font-family:'Open Sans',sans-serif}
.field-label{font-size:13px;color:var(--purple-deep);font-family:'Open Sans',sans-serif}
.form-a{left:620px;top:862px;width:400px}
.input{display:block;width:400px;height:22px;background:var(--white);border:1px solid var(--grey);margin:3px 0 8px}
.rose-btn{left:670px;top:965px;width:110px;height:26px;line-height:26px;font-size:17px}

/* cloth */
.cloth-photo{left:148px;top:1030px;width:542px;height:255px;background:linear-gradient(110deg,#d6d4d4,#3a8a86 45%,#1d5a63 70%,#e3e2e0)}
.cloth-box{left:690px;top:1045px;width:360px;height:230px;background:var(--blue-deep);color:var(--white);padding:16px 22px;font-size:17px;line-height:25px;overflow:hidden}

/* subscribe */
.heart{left:150px;top:1300px;width:140px;height:130px}
.heart-text{left:150px;top:1345px;width:140px;text-align:center;color:var(--white);font-size:15px;line-height:17px}
.chances{left:330px;top:1318px;width:660px;text-align:center;font-size:38px;line-height:50px;font-weight:400}
.sub-row{left:420px;top:1430px;display:flex;gap:0}
.sub-input{width:290px;height:26px;background:var(--white);border:1px solid var(--grey);font-size:15px;padding:3px 8px;color:var(--ink)}
.sub-btn{width:90px;height:26px;line-height:26px;font-size:15px;border-radius:0;background:var(--purple-deep)}

/* relax */
.relax-box{left:140px;top:1490px;width:460px;height:230px;background:var(--purple-deep);color:var(--white);padding:22px 26px;font-size:18px;line-height:27px;overflow:hidden}
.relax-photo{left:600px;top:1490px;width:400px;height:230px;background:linear-gradient(135deg,#d9d2c6,#6f5a4a 50%,#efe8dd)}

/* courses */
.courses-title{left:0;top:1752px;width:1200px;text-align:center;font-family:'Fjalla One',sans-serif;font-size:46px;font-weight:400;color:var(--ink)}
.course{top:1815px;width:210px;height:265px;background:var(--white)}
.course .pic{height:140px;background:linear-gradient(135deg,#5a4b40,#c7b79f)}
.course .info{height:125px;background:var(--purple);color:var(--white);padding:8px 14px;font-size:15px;line-height:19px;font-family:'Open Sans',sans-serif}
.course .price{font-weight:700}

/* pitch */
.pitch{left:150px;top:2092px;width:900px;text-align:center;font-family:'Fjalla One',sans-serif;font-size:31px;line-height:36px;color:var(--ink)}
.pitch-btn{left:500px;top:2248px;width:200px;height:40px;line-height:40px;font-size:28px}

/* article */
.banner{left:240px;top:2320px;width:720px;height:60px;background:var(--blue);color:var(--white);font-family:'Fjalla One',sans-serif;font-weight:400;font-size:38px;line-height:60px;text-align:center}
.product-art{left:360px;top:2395px;width:480px;height:250px;background:linear-gradient(90deg,#eaf6f8,#bfe6ee 50%,#eef1fb)}
.article-text{left:300px;top:2660px;width:600px;text-align:center;font-size:19px;line-height:22px}

.card{width:320px;background:rgba(255,255,255,.35);border:2px solid var(--purple)}
.card h3{height:40px;line-height:40px;text-align:center;color:var(--white);font-family:'Fjalla One',sans-serif;font-weight:400;font-size:22px;letter-spacing:.5px}
.card .h-purple{background:var(--purple)}
.card .h-blue{background:var(--blue)}
.card.b-blue{border-color:var(--blue)}
.card .lead{text-align:center;font-size:24px;margin:14px 0 16px}
.card p{font-family:'Open Sans',sans-serif;font-size:12px;line-height:17px;padding:0 22px}
.c1{left:220px;top:2860px;height:320px}
.c2{left:700px;top:2860px;height:320px}
.c3{left:220px;top:3250px;height:240px}
.c4{left:700px;top:3250px;height:240px}

.guide{left:240px;top:3540px;width:740px;border:2px solid var(--blue);background:rgba(255,255,255,.35)}
.guide h3{background:var(--blue);color:var(--white);text-align:center;font-family:'Fjalla One',sans-serif;font-weight:400;font-size:30px;height:50px;line-height:50px}
.guide p{text-align:center;font-size:20px;height:46px;line-height:46px}

/* footer */
.footer{left:0;top:3650px;width:1200px;height:74px;background:var(--footer);color:var(--white);font-family:'Open Sans',sans-serif;font-size:14px;font-weight:700}
.fcol{position:absolute;top:10px;line-height:18px;text-align:center}
.follow{left:660px;top:10px;text-align:center;font-size:12px}
.dots{display:flex;gap:10px;justify-content:center;margin-top:4px}
.dots span{width:16px;height:16px;border-radius:50%;background:var(--white);display:block}
</style>
</head>
<body>

<div class="abs hero photo" role="img" aria-label="Photo of a hello letter board with a coffee cup on a soft pink table"></div>
<nav class="abs nav">
  <a href="#">Home</a><a href="#">Blogs</a><a href="#">Contacts</a><a href="#">About Us</a><a href="#">Careers</a>
</nav>
<h1 class="abs hero-title">Gather Every Moment</h1>
<p class="abs hero-sub">Save TIME, MONEY and SANITY with simple product swaps.</p>
<a class="abs btn btn-green hero-btn">Sign up</a>

<div class="intro-photo photo" role="img" aria-label="Photo of friends sitting together on city steps with a dog"></div>
<p class="abs intro-text">Save TIME, MONEY and SANITY with<br>simple product swaps.<br>Reduce the amount of work it takes to<br>run your home.</p>
<a class="abs btn btn-purple intro-btn">SEE SAMPLE SWAP</a>

<div class="rose-photo photo" role="img" aria-label="Photo of a pink rose with white flowers"></div>
<p class="abs rose-text">Lorem ipsum dolor sit amet, consectetur adipiscing elit, sed do eiusmod tempor incididunt ut labore et dolore magna aliqua. Ut enim ad minim veniam, quis nostrud exercitation ullamco laboris nisi ut aliquip ex ea commodo consequat. Duis aute irure dolor in reprehenderit in voluptate velit esse cillum dolore eu fugiat nulla pariatur. Excepteur sint occaecat cupidatat non proident, sunt in culpa qui officia deserunt mollit anim id est laborum.</p>
<form class="abs form-a">
  <label class="field-label">Name</label><span class="input"></span>
  <label class="field-label">Email</label><span class="input"></span>
</form>
<a class="abs btn btn-green rose-btn">Sign Up</a>

<div class="cloth-photo photo" role="img" aria-label="Photo of a person shaking out a teal cloth over a bed"></div>
<p class="abs cloth-box">Lorem ipsum dolor sit amet, consectetur adipiscing elit, sed do eiusmod tempor incididunt ut labore et dolore magna aliqua. Ut enim ad minim veniam, quis nostrud exercitation ullamco laboris nisi ut aliquip ex ea commodo consequat. Duis aute.</p>

<svg class="abs heart" viewBox="0 0 140 130" aria-hidden="true"><path d="M70 125 C20 90 0 65 0 38 C0 15 18 0 38 0 C53 0 64 8 70 20 C76 8 87 0 102 0 C122 0 140 15 140 38 C140 65 120 90 70 125Z" fill="#3b9fd8"/></svg>
<p class="abs heart-text">Gather Every<br>Moment</p>
<p class="abs chances">Chances are life is a little overwhelming.<br>Let us help</p>
<div class="abs sub-row"><span class="sub-input">Email</span><a class="btn sub-btn">Subscribe</a></div>

<p class="abs relax-box">Lorem ipsum dolor sit amet, consectetur adipiscing elit, sed do eiusmod tempor incididunt ut labore et dolore magna aliqua. Ut enim ad minim veniam, quis nostrud exercitation ullamco laboris nisi ut aliquip ex ea commodo consequat. Duis aute irure dolor in reprehenderit in voluptate velit esse cillum.</p>
<div class="relax-photo photo" role="img" aria-label="Photo of a smiling woman lying among scattered photographs"></div>

<h2 class="abs courses-title">Courses</h2>
<div class="abs course" style="left:300px"><div class="pic" role="img" aria-label="Photo of a tidy kitchen shelf"></div><div class="info"><span class="price">$9 / month</span><br>Full access to all our courses with our monthly plan.</div></div>
<div class="abs course" style="left:540px"><div class="pic" role="img" aria-label="Photo of a warm lit dining table"></div><div class="info"><span class="price">$9 / month</span><br>Full access to all our courses with our monthly plan.</div></div>
<div class="abs course" style="left:780px"><div class="pic" role="img" aria-label="Photo of hands writing a weekly plan"></div><div class="info"><span class="price">$9 / month</span><br>Full access to all our courses with our monthly plan.</div></div>

<p class="abs pitch">Each swap save you work, clutter, time &amp; money.<br>You get an email 2x weekly for 6-12 weeks only<br>Get even more if you feel they are helpful to you<br>Join our monthly SIMPLE SWAP SHARING</p>
<a class="abs btn btn-green pitch-btn">Sign Me Up</a>

<h2 class="abs banner">Mouthwash for Tongue Scrapper</h2>
<div class="product-art photo" role="img" aria-label="Illustration of a crossed-out mouthwash bottle beside a tongue scraper"></div>
<p class="abs article-text">Tongue scrappers/cleaners are plastic or metal gadgets with arcs that help scrap off all the white stuff(bacteria) that gathered on your tongue in the morning.<br>The bacteria is responsible for most bad breath. So, if you use mouthwash primarily to freshen your breath, use before brushing your teeth to get the bacteria off your tongue.</p>

<section class="abs card c1"><h3 class="h-purple">CLUTTER SAVINGS:</h3><p class="lead">Plastic Bottle</p><p>The waste produced by mouthwash plastic bottles. Waste produced by a tongue scrubber/scraper is far less, and it lasts for months.</p></section>
<section class="abs card b-blue c2"><h3 class="h-blue">TIME SAVINGS:</h3><p class="lead">7-10 mins / Month</p><p>This includes the time used looking for, buying, disposing and recycling mouthwash. You will not have to buy it each month.</p></section>
<section class="abs card b-blue c3"><h3 class="h-blue">COST SAVINGS:</h3><p class="lead">$5-20 / Month</p><p>This will make a saving in a year for the family. A scraper costs about $5 and can be used for many months, while mouthwash runs out fast.</p></section>
<section class="abs card c4"><h3 class="h-purple">OTHER BENEFITS</h3><p class="lead">Plastic Bottle</p><p>Less waste produced by mouthwash plastic bottles. Waste made by tongue scrapers is far less.</p></section>

<section class="abs guide"><h3>BUYING GUIDE:</h3><p>Tongue Scrappers / Scrubbers on Shelfwise Market</p></section>

<footer class="abs footer">
  <div class="fcol" style="left:100px">FAQ<br>Terms Of Use<br>Contact Us</div>
  <div class="fcol" style="left:470px">Help Center<br>Jobs<br>Privacy</div>
  <div class="abs follow">Follow us<div class="dots"><span></span><span></span><span></span></div></div>
  <div class="fcol" style="left:900px">Account<br>Cookie Preferences<br>Legal Notices</div>
</footer>

</body>
</html>
```